Purple Envelope Campaign

I am after 2 flyers to promote a non profit, womens Christian organisation. Would like to put across a message to make people aware of the organisation and provide contact details. platform.
Target Market(s)
Women and Girls
Industry/Entity Type
Christian
Colors
ffc214
6b449b
Requirements
Must have
- I am after a clean but CATCHY design. Thinking of an envelope design. The main colours are purple and gold. The theme is 'THE GEM IN YOU'. It will be good to have a picture of a shining gem. I am after 2 flyers that target slightly different audiences. I have attached a photo of the logo, the wording required and a photo of Dr Nkemdirim Joy Halvorsenka, the founder of the Open Lantern Foundation. Printable flyer size is A5 and also images for use on social media.
Nice to have
- Purple envelope
- Shiny gem

```html
<!DOCTYPE html>
<html lang="en">
<head>
<meta charset="utf-8">
<title>The Gem In You – Flyers</title>
<link rel="stylesheet" href="https://fonts.googleapis.com/css2?family=Source+Sans+3:wght@400;600&family=Tinos:ital@1&display=swap">
<style>
  :root {
    --page-bg: #3b3b3d;
    --purple-deep: #2a0a30;
    --purple-mid: #5e1d6c;
    --purple-bright: #8a3398;
    --purple-brand: #6b449b;
    --jacket: #5a3d9a;
    --hair: #2a1c24;
    --gold: #ffc214;
    --gold-soft: #e9c77a;
    --gold-deep: #c98f24;
    --white: #ffffff;
    --ink: #141414;
    --phone: #6a2c8c;
  }
  * { margin: 0; padding: 0; box-sizing: border-box; }
  html, body { width: 902px; height: 1200px; overflow: hidden; }
  body { background: var(--page-bg); position: relative; }

  .flyer {
    position: absolute;
    left: 118px;
    width: 685px;
    height: 483px;
    overflow: hidden;
    background:
      radial-gradient(ellipse 420px 300px at 560px 140px, var(--purple-bright) 0%, rgba(138,51,152,0) 100%),
      radial-gradient(ellipse 380px 260px at 90px 380px, var(--purple-deep) 0%, rgba(42,10,48,0) 100%),
      linear-gradient(135deg, #4a1254 0%, var(--purple-mid) 45%, #7a2a8a 100%);
    box-shadow: 0 2px 6px rgba(0,0,0,.35);
  }
  .flyer--awareness { top: 88px; }
  .flyer--invitation { top: 640px; }

  .flyer__title {
    position: absolute;
    left: 74px;
    top: 24px;
    font-family: "Source Sans 3", sans-serif;
    font-weight: 400;
    font-size: 29px;
    letter-spacing: -0.3px;
    background: linear-gradient(180deg, #f6e3a8 0%, var(--gold-soft) 55%, var(--gold-deep) 100%);
    -webkit-background-clip: text;
    background-clip: text;
    color: transparent;
  }

  .flyer__body {
    position: absolute;
    left: 39px;
    top: 67px;
    width: 284px;
    font-family: "Tinos", serif;
    font-style: italic;
    font-size: 14px;
    line-height: 18.3px;
    color: var(--white);
    text-align: justify;
    hyphens: auto;
  }
  .flyer__body p { margin-bottom: 18.3px; }

  .flyer__portrait {
    position: absolute;
    left: 412px;
    top: 30px;
    width: 273px;
    height: 420px;
    border-radius: 136px 136px 0 0;
    background: linear-gradient(180deg, var(--hair) 0%, #3b2633 26%, #5b3e8c 50%, var(--jacket) 100%);
  }

  .flyer__waves { position: absolute; left: 0; top: 0; }

  .flyer__badge {
    position: absolute;
    left: 548px;
    top: 297px;
    width: 122px;
    height: 122px;
    border-radius: 50%;
    background: var(--white);
    border: 3px solid var(--gold-soft);
    display: flex;
    align-items: center;
    justify-content: center;
    font-family: "Source Sans 3", sans-serif;
    font-weight: 600;
    font-size: 15px;
    color: var(--purple-brand);
  }

  .flyer__contact {
    position: absolute;
    right: 13px;
    top: 420px;
    text-align: right;
    font-family: "Source Sans 3", sans-serif;
    font-weight: 600;
    font-size: 15px;
    line-height: 18.3px;
    color: var(--ink);
  }
  .flyer__phones { color: var(--phone); }
</style>
</head>
<body>

<section class="flyer flyer--awareness">
  <div class="flyer__portrait" role="img" aria-label="Portrait photo of the ministry founder in a purple jacket"></div>
  <svg class="flyer__waves" width="685" height="483" viewBox="0 0 685 483" aria-hidden="true">
    <defs>
      <linearGradient id="goldLineA" x1="0" x2="1">
        <stop offset="0" stop-color="#c98f24"/>
        <stop offset=".5" stop-color="#f3c65c"/>
        <stop offset="1" stop-color="#c98f24"/>
      </linearGradient>
    </defs>
    <path d="M0,430 C120,458 230,455 380,418 C480,394 580,374 685,366 L685,483 L0,483Z" fill="#4a1658"/>
    <path d="M0,423 C120,449 230,447 380,410 C480,386 580,366 685,358 L685,368 C580,376 480,396 380,420 C230,457 120,460 0,433Z" fill="url(#goldLineA)"/>
    <path d="M0,447 C120,472 240,470 390,430 C490,404 590,393 685,392 L685,483 L0,483Z" fill="#ffffff"/>
  </svg>
  <h1 class="flyer__title">THE GEM IN YOU</h1>
  <div class="flyer__body">
    <p>Women and girls are more precious than rubies; this is what God says about you and this is what we want to remind you about. Not only that but we want you to know that the Ministry of Bright Stones now operates under a newly launched international and non-denominational organization called Open Lantern Foundation.</p>
    <p>The Ministry’s founder and visionary Prophetess, Dr. Nkemdirim Joy Halvorsenka continues to provide visionary leadership. Find out what God is revealing. Be involved. Be a woman/girl of wisdom, wealth, good works, strength and honour, true beauty, excellence and one who fears the Lord.</p>
    <p>KEEP THAT GOD GIVEN VISION ALIVE.</p>
  </div>
  <div class="flyer__badge">Lumen Circle</div>
  <div class="flyer__contact">
    For more information please contact us on<br>
    <span class="flyer__phones">+263 770 418 205; +263 771906337</span><br>
    and follow us on Chatterbox and Pinwheel.
  </div>
</section>

<section class="flyer flyer--invitation">
  <div class="flyer__portrait" role="img" aria-label="Portrait photo of the ministry founder in a purple jacket"></div>
  <svg class="flyer__waves" width="685" height="483" viewBox="0 0 685 483" aria-hidden="true">
    <defs>
      <linearGradient id="goldLineB" x1="0" x2="1">
        <stop offset="0" stop-color="#c98f24"/>
        <stop offset=".5" stop-color="#f3c65c"/>
        <stop offset="1" stop-color="#c98f24"/>
      </linearGradient>
    </defs>
    <path d="M0,430 C120,458 230,455 380,418 C480,394 580,374 685,366 L685,483 L0,483Z" fill="#4a1658"/>
    <path d="M0,423 C120,449 230,447 380,410 C480,386 580,366 685,358 L685,368 C580,376 480,396 380,420 C230,457 120,460 0,433Z" fill="url(#goldLineB)"/>
    <path d="M0,447 C120,472 240,470 390,430 C490,404 590,393 685,392 L685,483 L0,483Z" fill="#ffffff"/>
  </svg>
  <h1 class="flyer__title">THE GEM IN YOU</h1>
  <div class="flyer__body">
    <p>Ladies do you know that God says you are very precious? In fact the bible says you are more precious than rubies.</p>
    <p>That’s very true, But do you believe that? Discover that true value and potential that God invested in you to transform you into a woman/girl of wisdom, wealth, good works, strength and honour, true beauty, excellence and one who fears the Lord under the leadership of Dr Nkemdirim Joy Halvorsenka.</p>
    <p>To find out more on how to unlock that true value and potential in you please contact us on +263 770 418 205; +263 771906337 and follow us on Chatterbox and Pinwheel.</p>
  </div>
  <div class="flyer__badge">Lumen Circle</div>
  <div class="flyer__contact">
    For more information please contact us on<br>
    <span class="flyer__phones">+263 770 418 205; +263 771906337</span><br>
    and follow us on Chatterbox and Pinwheel.
  </div>
</section>

</body>
</html>
```